Business card design needed for rebranded top-end landscaping business

We need a new business card design, incorporating our logo (colours Green #8dc63f and Grey #8a8c8e) and also some options that include the colour dark navy (eg #000040) as our uniforms are navy with white and grey trim.

We are an innovative landscaping company that maintains high-end gardens for meticulous clients. We pride ourselves on our customer service, our professionalism, and our workmanship.

Our business name needs to be easily read and our branding needs to be bold and memorable, without screaming "tradesman"! We prefer clean lines over lots of fine detail.

The design MUST include:
- Business name ("Brambleton Gardenworks")
- Logo (file uploaded)
- Employee name
- Phone number
- Email address
- www.brambletongardenworks.com.au
- Friendsnet & Snapgram logos
- The Turfcraft Guild logo (file uploaded) along with the word "Member"
- Licence "Lic. 618392K"

OPTIONAL inclusions:
- "Creating outdoor spaces for our community to be inspired, refreshed and re-energised"
- "Landscape Maintenance - Irrigation - Arboriculture" (dashes can be replaced with dots or other)
- "Fully qualified, licensed & insured"
- "Residential - Strata - Commercial - Real Estate" (dashes can be replaced with dots or other)

High-end professionals and retirees, real estate agents

Landscaping

See Project description

Sans Serif

Designer to choose colors to be used in the design.

• Must incorporate our logo, and colours Green #8dc63f and Grey #8a8c8e) from the logo, and the colour DARK NAVY (eg #000040).
• The design MUST include:
• - Business name ("Brambleton Gardenworks")
• - Logo (file uploaded)
• - Employee name
• - Phone number
• - Email address
• - www.brambletongardenworks.com.au
• - Friendsnet & Snapgram logos
• - The Turfcraft Guild logo (file uploaded) along with the word "Member"
• - Licence "Lic. 618392K"
• OPTIONAL inclusions:
• - "Creating outdoor spaces for our community to be inspired, refreshed and re-energised"
• - "Landscape Maintenance - Irrigation - Arboriculture" (dashes can be replaced with dots or other)
• - "Fully qualified, licensed & insured"
• - "Residential - Strata - Commercial - Real Estate" (dashes can be replaced with dots or other)

```html
<!DOCTYPE html>
<html lang="en">
<head>
<meta charset="utf-8">
<title>Brambleton Gardenworks – Business Card</title>
<link href="https://fonts.googleapis.com/css2?family=PT+Sans:wght@400;700&display=swap" rel="stylesheet">
<style>
  :root{
    --navy:#000040;
    --grey-band:#747474;
    --green:#7cff14;
    --brand-green:#8dc63f;
    --logo-grey:#8a8c8e;
    --ink:#0a0a4a;
    --white:#ffffff;
    --rule-lilac:#8a8cff;
    --page:#ffffff;
  }
  *{margin:0;padding:0;box-sizing:border-box}
  html,body{width:1200px;height:1000px;overflow:hidden;background:var(--page)}
  body{position:relative;font-family:"PT Sans",Arial,sans-serif;color:var(--ink)}
  .abs{position:absolute}
  .side-label{font-size:15px;font-weight:700;color:#000;top:327px}
  .card{position:absolute;top:350px;width:520px;height:319px;border:1px solid #333;overflow:hidden;background:var(--grey-band)}
  .card--front{left:57px}
  .card--back{left:626px}
  .band-navy{position:absolute;left:0;right:0;background:var(--navy)}

  /* front */
  .icon-rail{left:24px;top:36px;width:52px;height:266px;border-radius:26px;background:var(--green)}
  .icon-tile{left:13px;width:27px;height:27px;border-radius:5px;background:var(--white)}
  .icon-tile svg{display:block;width:27px;height:27px}
  .person-name{left:89px;top:47px;font-size:24px;color:var(--white)}
  .person-title{left:89px;top:82px;font-size:13px;color:var(--white)}
  .rule{left:89px;width:199px;height:1px}
  .contact{left:89px;font-size:14px;font-weight:700;color:var(--ink)}
  .contact--light{color:var(--white);font-weight:400}

  .brand{text-align:center}
  .brand-mark{border-radius:50%;border:7px solid var(--logo-grey)}
  .brand-name{font-weight:700;color:var(--brand-green);line-height:1}

  .social-dot{border-radius:50%;background:radial-gradient(circle at 40% 35%,#4a7ad8,#0b2a78 70%);box-shadow:0 0 0 2px #9aa3b8}
  .social-text{font-size:13px;font-weight:700;color:var(--ink)}
  .member{font-size:10px;font-weight:700;color:var(--ink)}
  .guild-badge{background:var(--brand-green);border-radius:3px}
  .licence{font-size:10px;font-weight:700;color:var(--ink)}
  .guild-rule{height:1px;background:#cfcfcf}

  /* back */
  .center-text{text-align:center;white-space:nowrap}
</style>
</head>
<body>

<div class="abs side-label" style="left:55px">BUSINESS CARD (FRONT)</div>
<div class="abs side-label" style="left:624px">BUSINESS CARD (BACK)</div>

<!-- FRONT -->
<section class="card card--front" aria-label="Business card front">
  <div class="band-navy" style="top:0;height:159px"></div>

  <div class="abs icon-rail">
    <div class="abs icon-tile" style="top:23px"><svg viewBox="0 0 27 27"><circle cx="13.5" cy="10" r="4.5" fill="var(--green)"/><path d="M5 21c1-5 4.5-6.5 8.5-6.5S21 16 22 21z" fill="var(--green)"/></svg></div>
    <div class="abs icon-tile" style="top:78px"><svg viewBox="0 0 27 27"><rect x="8" y="3.5" width="11" height="20" rx="2" fill="none" stroke="var(--green)" stroke-width="1.4"/><line x1="11.5" y1="20.5" x2="15.5" y2="20.5" stroke="var(--green)" stroke-width="1.2"/></svg></div>
    <div class="abs icon-tile" style="top:115px"><svg viewBox="0 0 27 27"><path d="M8 5l3 4-2 2c1 3 3 5 6 6l2-2 4 3-2 3c-7 0-13-6-13-13z" fill="none" stroke="var(--green)" stroke-width="1.4" stroke-linejoin="round"/></svg></div>
    <div class="abs icon-tile" style="top:152px"><svg viewBox="0 0 27 27"><rect x="4" y="7" width="19" height="13" fill="none" stroke="var(--green)" stroke-width="1.4"/><path d="M4 7l9.5 7L23 7" fill="none" stroke="var(--green)" stroke-width="1.4"/></svg></div>
    <div class="abs icon-tile" style="top:189px"><svg viewBox="0 0 27 27"><g fill="none" stroke="var(--green)" stroke-width="1.2"><circle cx="13.5" cy="13.5" r="9"/><ellipse cx="13.5" cy="13.5" rx="4" ry="9"/><line x1="4.5" y1="13.5" x2="22.5" y2="13.5"/><line x1="6" y1="9" x2="21" y2="9"/><line x1="6" y1="18" x2="21" y2="18"/></g></svg></div>
    <div class="abs icon-tile" style="top:226px"><svg viewBox="0 0 27 27"><path d="M13.5 23s-6-7-6-11.5a6 6 0 0 1 12 0C19.5 16 13.5 23 13.5 23z" fill="none" stroke="var(--green)" stroke-width="1.4"/><circle cx="13.5" cy="11.5" r="2.2" fill="none" stroke="var(--green)" stroke-width="1.2"/></svg></div>
  </div>

  <div class="abs person-name">Alex Marlow</div>
  <div class="abs rule" style="top:79px;background:var(--white)"></div>
  <div class="abs person-title">Owner/Project Manager</div>

  <div class="abs contact contact--light" style="top:121px">+00 (0) 0000 000000</div>
  <div class="abs rule" style="top:147px;background:var(--rule-lilac)"></div>
  <div class="abs contact" style="top:160px">+00 (0) 4183-927-560</div>
  <div class="abs rule" style="top:186px;background:#d8d8d8"></div>
  <div class="abs contact" style="top:194px">alex@brambleton.com.au</div>
  <div class="abs rule" style="top:222px;background:#d8d8d8"></div>
  <div class="abs contact" style="top:231px;font-size:13px">www.brambletongardenworks.com.au</div>
  <div class="abs rule" style="top:256px;background:#d8d8d8"></div>
  <div class="abs contact" style="top:260px;line-height:19px">214 Fern St #2, Ashgrove,<br>QLD 4060, Australia</div>

  <div class="abs brand" style="left:305px;top:22px;width:200px">
    <div class="brand-mark" style="width:60px;height:60px;margin:0 auto 8px"></div>
    <div class="brand-name" style="font-size:25px">Brambleton<br>Gardenworks</div>
  </div>

  <div class="abs social-dot" style="left:313px;top:170px;width:32px;height:32px"></div>
  <div class="abs social-text" style="left:361px;top:180px">brambleton.friendsnet.com</div>
  <div class="abs social-dot" style="left:313px;top:210px;width:32px;height:32px;background:radial-gradient(circle at 40% 35%,#8a5ae0,#3a1f9a 70%)"></div>
  <div class="abs social-text" style="left:361px;top:220px">brambleton.snapgram.com</div>

  <div class="abs member" style="left:311px;top:273px">Member:</div>
  <div class="abs guild-badge" style="left:418px;top:245px;width:20px;height:20px"></div>
  <div class="abs guild-rule" style="left:381px;top:272px;width:94px"></div>
  <div class="abs guild-rule" style="left:381px;top:286px;width:94px"></div>
  <div class="abs licence center-text" style="left:378px;top:292px;width:100px;font-size:9px">Licence "Lic. 618392K"</div>
</section>

<!-- BACK -->
<section class="card card--back" aria-label="Business card back">
  <div class="band-navy" style="top:0;height:159px"></div>
  <div class="band-navy" style="top:285px;height:34px"></div>

  <div class="abs brand" style="left:140px;top:26px;width:240px">
    <div class="brand-mark" style="width:64px;height:64px;margin:0 auto 10px"></div>
    <div class="brand-name" style="font-size:27px">Brambleton<br>Gardenworks</div>
  </div>

  <div class="abs social-dot" style="left:76px;top:168px;width:48px;height:48px"></div>
  <div class="abs social-text center-text" style="left:0;width:200px;top:224px">brambleton.friendsnet.com</div>
  <div class="abs social-dot" style="left:410px;top:168px;width:48px;height:48px;background:radial-gradient(circle at 40% 35%,#8a5ae0,#3a1f9a 70%)"></div>
  <div class="abs social-text center-text" style="left:334px;width:200px;top:224px">brambleton.snapgram.com</div>

  <div class="abs member center-text" style="left:210px;width:100px;top:166px">Member:</div>
  <div class="abs guild-badge" style="left:248px;top:181px;width:22px;height:22px"></div>
  <div class="abs guild-rule" style="left:200px;top:212px;width:118px"></div>
  <div class="abs guild-rule" style="left:200px;top:232px;width:118px"></div>
  <div class="abs licence center-text" style="left:190px;width:140px;top:239px;font-size:12px">Licence "Lic. 618392K"</div>

  <div class="abs social-text center-text" style="left:0;width:520px;top:262px;font-size:14px">www.brambletongardenworks.com.au</div>
  <div class="abs center-text" style="left:0;width:520px;top:292px;font-size:14px;color:var(--white)">214 Fern St #2, Ashgrove,&nbsp; QLD 4060, Australia</div>
</section>

</body>
</html>
```